Records Management Company Revamp

We are looking to revamp our web presence, and need a catchy design that helps us to get noticed! We would like the website to be in wordpress. the main requirements are a home page, a landing page template for SEO / PPC, and then a few other pages that can be reused throughout the website.

We are happy to supply content / video etc.
Updates

Low designer entries

Have guaranteed payment and hoping to receive more designs

Number of Pages Required

3 page

Other font styles liked:
• Find fonts listed in attached branding document

Requirements
Must have
• Home page as well as sub pages according to their colours. Need to use colours and fonts set out in branding guide. Attached are examples of home page and sub pages.
Nice to have
• We have uploaded some very basic ideas we have of how we wish the website to look, but looking to have it more professional and fit together. Please see uploaded items.

```html
<!DOCTYPE html>
<html lang="en">
<head>
<meta charset="utf-8">
<title>Vaultline Records – Records Management</title>
<link href="https://fonts.googleapis.com/css2?family=Poppins:wght@400;500;600&display=swap" rel="stylesheet">
<style>
:root{
  --red:#e5383f;
  --green:#8cc63e;
  --orange:#f39a1e;
  --sky:#7cb8e4;
  --blue:#1b9be0;
  --ink:#333a44;
  --muted:#7a818b;
  --line:#e3e6ea;
  --grey:#f2f2f2;
  --badge:#d9dde2;
  --white:#ffffff;
}
*{box-sizing:border-box;margin:0;padding:0}
html,body{width:1200px;height:4164px;overflow:hidden}
body{font-family:"Poppins",Arial,sans-serif;color:var(--ink);background:var(--white);position:relative}
.abs{position:absolute}
.btn{display:inline-block;background:var(--orange);color:var(--white);font-size:17px;font-weight:500;padding:12px 36px;border-radius:3px}

/* hero */
.hero{left:0;top:0;width:1200px;height:580px;background:linear-gradient(100deg,#3b3430 0%,#6a5a4c 45%,#4a3f37 100%)}
.brand{left:24px;top:24px;display:flex;align-items:center;gap:12px;font-size:30px;font-weight:600;color:var(--white)}
.brand-mark{width:34px;height:34px;background:var(--blue)}
.hero-title{left:96px;top:212px;width:600px;font-size:46px;line-height:1.18;font-weight:600;color:var(--white)}
.hero-sub{left:96px;top:400px;width:600px;font-size:22px;line-height:1.3;color:var(--white)}

/* quote form */
.quote{left:720px;top:0;width:464px;height:640px;background:var(--white);border:2px solid var(--blue);padding:34px 42px;box-shadow:0 6px 20px rgba(0,0,0,.15)}
.quote-badge{left:208px;top:-2px;width:44px;height:40px;background:var(--red)}
.quote h2{text-align:center;color:var(--red);font-size:34px;font-weight:600;margin-top:54px}
.quote .intro{text-align:center;font-size:12px;color:var(--muted);margin:6px 0 20px}
.field label{display:block;font-size:11px;font-weight:600;margin-bottom:4px}
.field .box{height:40px;border:1px solid var(--line);margin-bottom:14px}
.field .box.tall{height:60px}
.quote .btn{display:block;text-align:center;margin-top:8px}
.quote .legal{font-size:11px;color:var(--muted);margin-top:12px;line-height:1.4}

/* services */
.photo{border-radius:50%;border:12px solid}
.service h2{font-size:46px;font-weight:500;line-height:1.3}
.service .sub{font-size:13px;letter-spacing:4px;color:#b9bec5;margin:2px 0 16px}
.service p{font-size:14px;color:var(--muted);line-height:1.6;width:520px}
.ticks{list-style:none;margin-top:18px}
.ticks li{display:flex;align-items:center;gap:14px;font-size:16px;line-height:1.4;margin-bottom:12px}
.ticks li:last-child{margin-bottom:0}
.divider{left:140px;width:920px;height:1px;background:var(--line)}

/* accreditation */
.accred{left:0;top:2560px;width:1200px;height:400px;background:var(--grey);text-align:center}
.accred h2{margin-top:60px;color:var(--green);font-size:30px;font-weight:600}
.badges{display:flex;justify-content:center;gap:70px;margin-top:36px}
.badge{width:150px;height:80px;border-radius:8px;background:var(--badge)}
.accred p{font-size:13px;color:var(--muted);margin:30px auto 20px;width:520px}

/* about */
.about-band{left:288px;top:2960px;width:912px;height:440px;background:var(--blue)}
.about-visual{left:0;top:2990px;width:640px;height:420px;background:linear-gradient(160deg,#cfd6de,#8e9aa8);border-radius:10px}
.about-text{left:660px;top:3040px;width:510px;color:var(--white)}
.about-text h2{font-size:38px;font-weight:500;white-space:nowrap}
.about-text .sub{font-size:13px;letter-spacing:4px;margin:4px 0 20px;opacity:.85}
.about-text p{font-size:14px;line-height:1.6;margin-bottom:14px}

/* benefits */
.benefits-title{left:0;top:3516px;width:1200px;text-align:center;color:var(--blue);font-size:30px;font-weight:600}
.grid{left:180px;top:3610px;width:840px;display:grid;grid-template-columns:1fr 1fr;border:1px solid var(--line)}
.cell{display:flex;gap:24px;align-items:center;padding:24px 28px;border:1px solid var(--line);font-size:13px;color:var(--muted);line-height:1.5;height:120px}
.cell svg{flex:none}

/* cta */
.cta{left:0;top:3848px;width:1200px;height:316px;background:linear-gradient(180deg,#2a2e33,#15181b);text-align:center;color:var(--white)}
.cta h2{margin-top:110px;font-size:38px;font-weight:500}
.cta p{font-size:14px;opacity:.8;margin:10px auto 20px;width:560px}
</style>
</head>
<body>

<section class="hero abs" role="img" aria-label="Warehouse aisle stacked with archive boxes"></section>
<div class="brand abs"><span class="brand-mark"></span>Vaultline Records</div>
<h1 class="hero-title abs">Lorem Ipsum is simply dummy text for printing industry.</h1>
<p class="hero-sub abs">There are many variations of passages of Lorem Ipsum</p>

<aside class="quote abs">
  <div class="quote-badge abs"></div>
  <h2>Get A FREE Quote!</h2>
  <p class="intro">It is a long established fact that a reader will be distracted by the readable content of a page.</p>
  <div class="field"><label>FIRST NAME*</label><div class="box"></div></div>
  <div class="field"><label>PHONE*</label><div class="box"></div></div>
  <div class="field"><label>EMAIL*</label><div class="box"></div></div>
  <div class="field"><label>MESSAGE*</label><div class="box tall"></div></div>
  <span class="btn">Get A Quote Now</span>
  <p class="legal">By submitting this form you are confirming you have read and agree to our Terms of Use and Privacy Policy.</p>
</aside>

<svg width="0" height="0" style="position:absolute">
  <symbol id="tick" viewBox="0 0 24 24"><path d="M3 12l6 6L21 5" fill="none" stroke="#333a44" stroke-width="2.4"/></symbol>
</svg>

<!-- offsite storage -->
<div class="photo abs" style="left:152px;top:740px;width:328px;height:328px;border-color:var(--red);background:linear-gradient(135deg,#c9a77a,#6c5a49)" role="img" aria-label="Warehouse racking with forklift"></div>
<div class="service abs" style="left:548px;top:768px">
  <h2 style="color:var(--red)">Offsite Storage</h2>
  <div class="sub">LOREM IPSUM DUMMY PRINTING TEXT</div>
  <p>Lorem ipsum dolor sit amet, consectetur adipiscing elit, sed do eiusmod tempor incididunt ut labore et dolore magna aliqua. Ut enim ad minim veniam, quis nostrud exercitation ullamco laboris.</p>
  <ul class="ticks">
    <li><svg width="22" height="22"><use href="#tick"/></svg>Lorem ipsum dolor sit amet consectet.</li>
    <li><svg width="22" height="22"><use href="#tick"/></svg>Sed ut perspiciatis unde omnis iste natus error sit voluptatem.</li>
    <li><svg width="22" height="22"><use href="#tick"/></svg>At vero eos et accusamus et iusto odio dignissimos.</li>
  </ul>
</div>
<div class="divider abs" style="top:1128px"></div>

<!-- document shredding -->
<div class="service abs" style="left:148px;top:1190px">
  <h2 style="color:var(--green)">Document Shredding</h2>
  <div class="sub">LOREM IPSUM DUMMY PRINTING TEXT</div>
  <p>Lorem ipsum dolor sit amet, consectetur adipiscing elit, sed do eiusmod tempor incididunt ut labore et dolore magna aliqua. Ut enim ad minim veniam, quis nostrud exercitation ullamco laboris.</p>
  <ul class="ticks">
    <li><svg width="22" height="22"><use href="#tick"/></svg>Lorem ipsum dolor sit amet consectet.</li>
    <li><svg width="22" height="22"><use href="#tick"/></svg>Sed ut perspiciatis unde omnis iste natus error sit voluptatem.</li>
    <li><svg width="22" height="22"><use href="#tick"/></svg>At vero eos et accusamus et iusto odio dignissimos.</li>
  </ul>
</div>
<div class="photo abs" style="left:720px;top:1140px;width:328px;height:328px;border-color:var(--green);background:linear-gradient(135deg,#dfe3e6,#9aa2a8)" role="img" aria-label="Pile of shredded paper"></div>
<span class="btn abs" style="left:532px;top:1594px">Get A Quote Now</span>

<!-- digitisation -->
<div class="photo abs" style="left:152px;top:1720px;width:328px;height:328px;border-color:var(--orange);background:linear-gradient(135deg,#e0b04a,#8a6a3e)" role="img" aria-label="Worker scanning archive boxes on shelves"></div>
<div class="service abs" style="left:548px;top:1750px">
  <h2 style="color:var(--orange)">Digitisation</h2>
  <div class="sub">LOREM IPSUM DUMMY PRINTING TEXT</div>
  <p>Lorem ipsum dolor sit amet, consectetur adipiscing elit, sed do eiusmod tempor incididunt ut labore et dolore magna aliqua. Ut enim ad minim veniam, quis nostrud exercitation ullamco laboris.</p>
  <ul class="ticks">
    <li><svg width="22" height="22"><use href="#tick"/></svg>Lorem ipsum dolor sit amet consectet.</li>
    <li><svg width="22" height="22"><use href="#tick"/></svg>Sed ut perspiciatis unde omnis iste natus error sit voluptatem.</li>
    <li><svg width="22" height="22"><use href="#tick"/></svg>At vero eos et accusamus et iusto odio dignissimos.</li>
  </ul>
</div>
<div class="divider abs" style="top:2112px"></div>

<!-- archiving supplies -->
<div class="service abs" style="left:148px;top:2186px">
  <h2 style="color:var(--sky)">Archiving Supplies</h2>
  <div class="sub">LOREM IPSUM DUMMY PRINTING TEXT</div>
  <p>Lorem ipsum dolor sit amet, consectetur adipiscing elit, sed do eiusmod tempor incididunt ut labore et dolore magna aliqua. Ut enim ad minim veniam, quis nostrud exercitation ullamco laboris.</p>
  <ul class="ticks">
    <li><svg width="22" height="22"><use href="#tick"/></svg>Lorem ipsum dolor sit amet consectet.</li>
    <li><svg width="22" height="22"><use href="#tick"/></svg>Sed ut perspiciatis unde omnis iste natus error sit voluptatem.</li>
    <li><svg width="22" height="22"><use href="#tick"/></svg>At vero eos et accusamus et iusto odio dignissimos.</li>
  </ul>
</div>
<div class="photo abs" style="left:720px;top:2164px;width:328px;height:328px;border-color:var(--sky);background:linear-gradient(135deg,#cdb48c,#3e6aa6)" role="img" aria-label="Courier carrying stacked cardboard boxes"></div>

<!-- accreditation -->
<section class="accred abs">
  <h2>Our Accreditation</h2>
  <div class="badges"><div class="badge"></div><div class="badge"></div></div>
  <p>It is a long established fact that a reader will be distracted by the readable content of a page when looking at its layout.</p>
  <span class="btn">Get A Quote Now</span>
</section>

<!-- about -->
<div class="about-band abs"></div>
<div class="about-visual abs" role="img" aria-label="Laptop displaying the company website"></div>
<div class="about-text abs">
  <h2>About Vaultline Records</h2>
  <div class="sub">LOREM IPSUM DUMMY PRINTING TEXT</div>
  <p>Lorem ipsum dolor sit amet, consectetur adipiscing elit, sed do eiusmod tempor incididunt ut labore et dolore magna aliqua. Ut enim ad minim veniam, quis nostrud exercitation ullamco.</p>
  <p>Lorem Ipsum is simply dummy text of the printing and typesetting industry. Lorem Ipsum has been the industry standard dummy text.</p>
</div>

<!-- benefits -->
<h2 class="benefits-title abs">What are the benefits with us:</h2>
<div class="grid abs">
  <div class="cell"><svg width="44" height="44" viewBox="0 0 44 44" fill="none" stroke="#9aa1aa" stroke-width="2"><rect x="6" y="8" width="32" height="28"/><path d="M6 16h32"/></svg>Lorem ipsum dolor sit amet, consectetur. Sed do eiusmod tempor incididunt ut labore et dolore magna aliqua.</div>
  <div class="cell"><svg width="44" height="44" viewBox="0 0 44 44" fill="none" stroke="#9aa1aa" stroke-width="2"><rect x="10" y="4" width="24" height="36"/><path d="M15 14h14M15 22h14M15 30h10"/></svg>All the Lorem Ipsum generators on the Internet tend to repeat predefined chunks as necessary.</div>
  <div class="cell"><svg width="44" height="44" viewBox="0 0 44 44" fill="none" stroke="#9aa1aa" stroke-width="2"><rect x="4" y="10" width="36" height="24"/><path d="M4 10l18 14 18-14"/></svg>It uses a dictionary of over 200 Latin words, combined with a handful of model sentence structures.</div>
  <div class="cell"><svg width="44" height="44" viewBox="0 0 44 44" fill="none" stroke="#9aa1aa" stroke-width="2"><circle cx="22" cy="22" r="16"/><path d="M22 12v10l7 5"/></svg>The generated Lorem Ipsum is therefore always free from repetition, injected humour or words.</div>
</div>

<!-- call to action -->
<section class="cta abs" role="img" aria-label="Dimmed warehouse backdrop">
  <h2>What are you waiting for?</h2>
  <p>The generated Lorem Ipsum is therefore always free from repetition, injected humour, or non-characteristic words etc.</p>
  <span class="btn">Get A Quote Now</span>
</section>

</body>
</html>
```